Business Card Design Project

commercial exhaust hood cleaning and kitchen cleaning

Industry/Entity Type

Business

Contact Information for Business Card

a logo and name on front

```html
<!DOCTYPE html>
<html lang="en">
<head>
<meta charset="utf-8">
<title>Business Card – Front</title>
<link rel="stylesheet" href="https://fonts.googleapis.com/css2?family=Open+Sans:ital,wght@0,400;0,700;0,800;1,400&display=swap">
<style>
  :root {
    --brand-red: #b0182b;
    --band-grey: #a3a5a8;
    --ink: #3d3d3d;
    --ink-soft: #555658;
    --card: #ffffff;
    --backdrop: #e8e8e8;
  }
  * { box-sizing: border-box; margin: 0; padding: 0; }
  html, body {
    width: 1200px;
    height: 1000px;
    overflow: hidden;
    background: var(--backdrop);
    font-family: "Open Sans", Arial, sans-serif;
  }
  .business-card {
    position: absolute;
    left: 100px;
    top: 218px;
    width: 1000px;
    height: 563px;
    background: var(--card);
    box-shadow: 0 6px 24px rgba(0,0,0,0.18);
    overflow: hidden;
  }
  .card-bands {
    position: absolute;
    inset: 0;
    width: 1000px;
    height: 563px;
  }
  .band-grey { fill: var(--band-grey); }
  .band-red { fill: var(--brand-red); }

  .brand-name {
    position: absolute;
    left: 58px;
    top: 118px;
    font-weight: 800;
    font-size: 86px;
    line-height: 1;
    color: var(--brand-red);
    letter-spacing: 1px;
  }
  .person {
    position: absolute;
    left: 62px;
    top: 378px;
    color: var(--ink-soft);
  }
  .person-name {
    font-style: italic;
    font-size: 40px;
    line-height: 1.1;
  }
  .person-role {
    font-size: 21px;
    margin-top: 2px;
    color: var(--ink);
  }
  .contact {
    position: absolute;
    left: 698px;
    top: 256px;
    color: var(--ink);
    font-size: 21px;
    line-height: 30px;
  }
  .address { margin-bottom: 26px; }
  .contact-list { list-style: none; }
  .contact-item {
    display: flex;
    align-items: center;
    height: 36px;
  }
  .contact-icon {
    width: 22px;
    height: 22px;
    margin-right: 22px;
    flex: none;
  }
  .contact-icon rect.tile { fill: var(--ink); }
  .contact-icon .glyph { fill: #ffffff; }
  .website {
    position: absolute;
    left: 698px;
    top: 486px;
    color: #ffffff;
    font-size: 21px;
    letter-spacing: 0.3px;
  }
</style>
</head>
<body>
  <main class="business-card">
    <svg class="card-bands" viewBox="0 0 1000 563" aria-hidden="true">
      <path class="band-grey" d="M0 498 H540 C575 498 585 476 620 476 H1000 V563 H0 Z"/>
      <path class="band-red" d="M0 521 H555 C592 521 598 474 640 474 H1000 V563 H0 Z"/>
    </svg>

    <div class="brand-name">Logo Here</div>

    <div class="person">
      <p class="person-name">Name Title</p>
      <p class="person-role">designation</p>
    </div>

    <div class="contact">
      <p class="address">suit # 00, Lorem ipsum<br>Lorem Lorem ipsum</p>
      <ul class="contact-list">
        <li class="contact-item">
          <svg class="contact-icon" viewBox="0 0 22 22" aria-label="Phone">
            <rect class="tile" width="22" height="22" rx="3"/>
            <path class="glyph" d="M7 4 L9.5 4 L10.5 8 L8.8 9.2 C9.6 11 11 12.4 12.8 13.2 L14 11.5 L18 12.5 L18 15 C18 16.5 16.5 17.5 15 17 C10 15.5 6.5 12 5 7 C4.5 5.5 5.5 4 7 4 Z"/>
          </svg>
          <span>000-000-0000</span>
        </li>
        <li class="contact-item">
          <svg class="contact-icon" viewBox="0 0 22 22" aria-label="Fax">
            <rect class="tile" width="22" height="22" rx="3" fill="none"/>
            <rect x="6" y="2" width="10" height="7" fill="#3d3d3d"/>
            <rect x="2" y="9" width="18" height="9" rx="1.5" fill="#3d3d3d"/>
            <rect x="6" y="13" width="10" height="7" fill="#3d3d3d" stroke="#fff" stroke-width="1.2"/>
          </svg>
          <span>000-000-0000</span>
        </li>
        <li class="contact-item">
          <svg class="contact-icon" viewBox="0 0 22 22" aria-label="Email">
            <path d="M2 9 L11 3 L20 9 V19 H2 Z" fill="#3d3d3d"/>
            <path d="M3 10 L11 15 L19 10" fill="none" stroke="#fff" stroke-width="1.5"/>
          </svg>
          <span>abcd@example.com</span>
        </li>
      </ul>
    </div>

    <p class="website">www.example.com.au</p>
  </main>
</body>
</html>
```